New Business Card for Software Company

We are looking at rebranding a 10 year old company that specializes in PDF and DWF solutions for Architects and Engineers. We will attach the new company logo that we are going with so you can work with that and complimentary colors.
The sample information we would like on the business card is:
Gerald Pembrook
Vice President
4173 W. Tillman Avenue. STE 306
PMB#417
Mesa, AZ 85316
866-392-7154 US Toll Free
123-581-3064 Cell
gpembrook@vextrolan.com
The old tag line that we had on the business cars was.
Providing Industrial Strength PDF and DWF Solutions to the Global CAD Marketplace.
If you have an idea for a better tag line we are open to that also.
Updates
We would like to thank all of the Designers for their wonderful work. We apologize that we will not have the time to provide feedback to everyone. There is just so many innovative and professional designs that you have all created making our decision even harder.
Target Market(s)
Architects and Engineers
Industry/Entity Type
Business
Look and feel
Each slider illustrates characteristics of the customer's brand and the style your logo design should communicate.

```html
<!DOCTYPE html>
<html lang="en">
<head>
<meta charset="utf-8">
<title>Gerald Pembrook – Business Card</title>
<link rel="stylesheet" href="https://fonts.googleapis.com/css2?family=Arimo:wght@400;700&display=swap">
<style>
  :root {
    --card-bg: #ffffff;
    --band-red: #c62a2f;
    --band-mid: #ee5a28;
    --band-orange: #f7911f;
    --ink-light: #ffffff;
  }
  html, body {
    margin: 0;
    padding: 0;
    overflow: hidden;
    background: var(--card-bg);
  }
  .card {
    position: relative;
    width: 1200px;
    height: 637px;
    overflow: hidden;
    background: var(--card-bg);
    font-family: "Arimo", Helvetica, Arial, sans-serif;
    color: var(--ink-light);
  }
  .card__band {
    position: absolute;
    inset: 0;
    width: 1200px;
    height: 637px;
  }
  .identity {
    position: absolute;
    left: 134px;
    top: 170px;
    margin: 0;
    font-size: 34px;
    font-weight: 400;
    line-height: 1;
    white-space: nowrap;
  }
  .identity__name { font-weight: 700; }
  .contact {
    position: absolute;
    left: 134px;
    top: 260px;
    margin: 0;
    font-size: 34px;
    line-height: 44px;
    display: grid;
    grid-template-columns: 222px auto;
    white-space: nowrap;
  }
  .contact dt, .contact dd { margin: 0; }
  .address {
    position: absolute;
    right: 66px;
    top: 446px;
    margin: 0;
    font-style: normal;
    font-size: 34px;
    line-height: 48px;
    text-align: right;
    white-space: nowrap;
  }
</style>
</head>
<body>
<main class="card">
  <svg class="card__band" viewBox="0 0 1200 637" aria-hidden="true">
    <defs>
      <linearGradient id="bandGradient" x1="0" y1="0" x2="1" y2="0">
        <stop offset="0" stop-color="var(--band-red)"/>
        <stop offset="0.55" stop-color="var(--band-mid)"/>
        <stop offset="1" stop-color="var(--band-orange)"/>
      </linearGradient>
    </defs>
    <polygon points="0,120 408,0 1098,60 1200,498 1200,637 108,574" fill="url(#bandGradient)"/>
  </svg>

  <p class="identity"><span class="identity__name">Gerald Pembrook</span> Vice President</p>

  <dl class="contact">
    <dt>US Toll Free</dt><dd>866 392 7154</dd>
    <dt>Cell Phone</dt><dd>123 581 3064</dd>
    <dt>Email</dt><dd>gpembrook@vextrolan.com</dd>
  </dl>

  <address class="address">
    4173 W. Tillman Avenue<br>
    STE 306 PMB#417<br>
    Mesa, AZ 85316
  </address>
</main>
</body>
</html>
```